依頼詳細
・縦長名刺サイズ三つ折り
・ブライダル関係とわかる写真入り(例:夕日をバックに二人のシルエット等)
・まずは無料カウンセリングの表記
・人生を豊かに。
結婚への意欲を促す文章
・QRコード記載(作成中なので仮で入れてください)
・圧倒的な成婚達成の実績
・成婚達成に導く「4つのサポート」
質の良い出会いと数 (説明文入れるスペース)
プロ集団のサポート (         )
交際フォロー    (         )
メンタルサポート  (         )
・ご成約保証制度
・緑風ご縁協会(蒼取一部上場企業)加盟店
・選べる4つのコース コースが4つあります

記載項目
ロゴデータ添付いたします
サイズ
名刺サイズ
ページ数
両面
希望イメージ
シンプル 複雑
単色 カラフル
暗い 明るい
日常 高級
遊び心 厳粛
未来的 伝統的
女性的 男性的
希望する色
黄・オレンジ系、グレー系
納品ファイル
• 高解像度JPG (.jpg)
• イラストレーター形式 (.ai)
• フォトショップ形式 (.psd)
• PNG形式 (.png)
補足説明

高級感があり、イメージどおりのデザインでした!
いくつか修正お願いしますが、よろしくお願いします!

ありがとうございます!
とても気に入りました!

```html
<!DOCTYPE html>
<html lang="ja">
<head>
<meta charset="utf-8">
<title>縁結びラボ 名刺</title>
<link rel="stylesheet" href="https://fonts.googleapis.com/css2?family=Noto+Sans+JP:wght@400;500;700&family=Noto+Serif+JP:wght@400;600;700;900&display=swap">
<style>
  :root {
    --bg: #0a0a0a;
    --gold: #c9a35a;
    --gold-light: #e8cf92;
    --gold-deep: #9c7a3a;
    --white: #f4f1ea;
    --grey: #a9a49b;
    --fold: #1e1e1e;
  }
  * { margin: 0; padding: 0; box-sizing: border-box; }
  html, body { width: 1200px; height: 2176px; overflow: hidden; background: var(--bg); }
  body { position: relative; font-family: "Noto Sans JP", sans-serif; color: var(--white); }

  /* ---------- front panel ---------- */
  .card-front { position: absolute; left: 0; top: 0; width: 1200px; height: 740px; }

  .brand { position: absolute; left: 150px; top: 110px; width: 320px; display: flex; flex-direction: column; align-items: center; }
  .brand-dot { width: 150px; height: 150px; border-radius: 50%; background: var(--gold); }
  .brand-sub { margin-top: 26px; font-family: "Noto Serif JP", serif; font-size: 32px; letter-spacing: 3px; color: var(--gold); }
  .brand-name { margin-top: 4px; font-family: "Noto Serif JP", serif; font-weight: 600; font-size: 54px; letter-spacing: 3px; color: var(--gold); }

  .person { position: absolute; left: 540px; top: 206px; }
  .person-role { font-size: 30px; font-weight: 700; }
  .person-roman { margin-top: 30px; font-size: 26px; letter-spacing: 4px; word-spacing: 70px; }
  .person-name { margin-top: 2px; font-size: 78px; font-weight: 700; letter-spacing: 8px; line-height: 1.2; }
  .member { margin-top: 26px; font-size: 22px; color: var(--gold); letter-spacing: 1px; }

  .contact { position: absolute; left: 72px; width: 1080px; font-size: 25px; display: flex; }
  .contact span:first-child { width: 680px; }
  .contact.row1 { top: 604px; }
  .contact.row2 { top: 652px; }

  .fold-line { position: absolute; left: 0; top: 740px; width: 1200px; height: 2px; background: var(--fold); }

  /* ---------- inner panel ---------- */
  .tagline { position: absolute; top: 806px; width: 100%; text-align: center; font-family: "Noto Serif JP", serif; font-weight: 600; font-size: 42px; letter-spacing: 12px; color: var(--gold); }

  .photo { position: absolute; }
  .photo-couple { left: 340px; top: 900px; width: 660px; height: 680px;
    background: radial-gradient(closest-side, #ebe8e3 0%, #bcb5ad 45%, #5a534e 75%, rgba(10,10,10,0) 100%); }
  .photo-left { left: 70px; top: 930px; width: 250px; height: 280px;
    background: radial-gradient(closest-side, #dcdad6 0%, #7a7571 55%, rgba(10,10,10,0) 100%); }
  .photo-right { left: 920px; top: 930px; width: 200px; height: 280px;
    background: radial-gradient(closest-side, #d3cec8 0%, #716b66 55%, rgba(10,10,10,0) 100%); }

  .info-list { position: absolute; top: 1250px; }
  .info-list h3 { font-family: "Noto Serif JP", serif; font-weight: 700; font-size: 26px; color: var(--gold); margin-bottom: 12px; letter-spacing: 1px; }
  .info-list li { list-style: none; font-size: 20px; line-height: 1.3; color: var(--white); margin-bottom: 10px; }
  .info-list li small { display: block; font-size: 16px; color: var(--grey); }
  .support-list { left: 60px; width: 270px; }
  .course-list { left: 1000px; width: 170px; }

  .result { position: absolute; top: 1610px; left: 300px; display: flex; align-items: center; gap: 28px; }
  .result-label { font-family: "Noto Serif JP", serif; color: var(--gold); text-align: center; }
  .result-label .big { font-size: 86px; font-weight: 900; line-height: 1; letter-spacing: 6px; }
  .result-label .small { font-size: 40px; font-weight: 700; letter-spacing: 4px; margin-top: 6px; }
  .result-num { font-family: "Noto Serif JP", serif; font-weight: 700; font-size: 170px; line-height: 1;
    background: linear-gradient(180deg, var(--gold-light), var(--gold) 55%, var(--gold-deep));
    -webkit-background-clip: text; background-clip: text; color: transparent; }
  .result-num .pct { font-size: 96px; }

  .guarantee { position: absolute; top: 1836px; width: 100%; text-align: center; font-family: "Noto Serif JP", serif; font-weight: 700; font-size: 38px; letter-spacing: 4px; color: var(--gold); }

  .cta { position: absolute; left: 192px; top: 1918px; width: 828px; height: 76px; border: 3px solid var(--gold);
    display: flex; align-items: center; justify-content: center; font-weight: 500; font-size: 36px; letter-spacing: 8px; color: var(--gold); }

  .phone { position: absolute; top: 2050px; left: 330px; display: flex; align-items: center; gap: 22px;
    font-family: "Noto Serif JP", serif; font-weight: 600; font-size: 62px; letter-spacing: 4px; color: var(--gold); }
  .phone svg { width: 56px; height: 56px; }

  .qr { position: absolute; left: 1050px; top: 2010px; width: 120px; height: 120px; border: 3px solid var(--gold);
    display: flex; align-items: center; justify-content: center; font-size: 18px; color: var(--gold); text-align: center; line-height: 1.3; }
</style>
</head>
<body>
  <section class="card-front">
    <div class="brand">
      <span class="brand-dot"></span>
      <span class="brand-sub">BRIDAL STUDIO</span>
      <span class="brand-name">縁結びラボ</span>
    </div>

    <div class="person">
      <div class="person-role">成婚アドバイザー</div>
      <div class="person-roman">Sato Ichiro</div>
      <div class="person-name">佐藤 一郎</div>
      <div class="member">緑風ご縁協会(蒼取一部上場企業)加盟店</div>
    </div>

    <div class="contact row1">
      <span>〒100-0001 東京都みどり市さくら町1-2-3</span>
      <span>https://○○○○○.com</span>
    </div>
    <div class="contact row2">
      <span>TEL.01-9876-5432 FAX.01-9876-5433</span>
      <span>○○○○○@○○○○.com</span>
    </div>
  </section>

  <div class="fold-line"></div>

  <p class="tagline">結婚で豊かな人生を。</p>

  <div class="photo photo-left" role="img" aria-label="一人でうずくまる男性の写真"></div>
  <div class="photo photo-couple" role="img" aria-label="ブーケを持つ新郎新婦の写真"></div>
  <div class="photo photo-right" role="img" aria-label="膝を抱えて座る女性の写真"></div>

  <div class="info-list support-list">
    <h3>4つのサポート</h3>
    <ul>
      <li>質の良い出会いと数<small>厳選された出会いを多数ご紹介</small></li>
      <li>プロ集団のサポート<small>経験豊富な専門家が伴走</small></li>
      <li>交際フォロー<small>交際中も細やかにフォロー</small></li>
      <li>メンタルサポート<small>不安な気持ちに寄り添います</small></li>
    </ul>
  </div>

  <div class="info-list course-list">
    <h3>選べる4コース</h3>
    <ul>
      <li>ライト</li>
      <li>スタンダード</li>
      <li>プレミアム</li>
      <li>エグゼクティブ</li>
    </ul>
  </div>

  <div class="result">
    <div class="result-label">
      <div class="big">成婚</div>
      <div class="small">達成実績</div>
    </div>
    <div class="result-num">92<span class="pct">%</span></div>
  </div>

  <p class="guarantee">ご成約保証制度</p>

  <div class="cta">まずは無料カウンセリング</div>

  <div class="phone">
    <svg viewBox="0 0 24 24" aria-hidden="true">
      <path fill="#c9a35a" d="M6.6 10.8a15.1 15.1 0 0 0 6.6 6.6l2.2-2.2c.3-.3.7-.4 1-.2 1.1.4 2.3.6 3.6.6.6 0 1 .4 1 1V20c0 .6-.4 1-1 1A17 17 0 0 1 3 4c0-.6.4-1 1-1h3.5c.6 0 1 .4 1 1 0 1.3.2 2.5.6 3.6.1.3 0 .7-.2 1z"/>
    </svg>
    <span>01-987-6543</span>
  </div>

  <div class="qr" role="img" aria-label="QRコード配置予定">QR<br>コード</div>
</body>
</html>
```